RV park billboard

We need a billboard for cedar bend RV park . I was thinking about having a big orange in the background. We will have free fiber optic internet and each camper will have its own personal hotspot and we want that on the sign... Also the phone number with the area code... But I don't have the exact number yet. Size of sign will be 12 x 40
Make sure sign has Cedar Bend RV park on it
Plant turnaround workers

```html
<!DOCTYPE html>
<html lang="en">
<head>
<meta charset="utf-8">
<title>Cedar Bend RV Park – Billboard</title>
<link rel="stylesheet" href="https://fonts.googleapis.com/css2?family=Anton&family=Barlow+Condensed:ital,wght@1,700&display=swap">
<style>
  :root {
    --page: #f4f4f4;
    --white: #ffffff;
    --orange-bright: #ffa000;
    --orange-deep: #ee9232;
    --orange-red: #ff6a00;
    --peach: #f5c690;
    --fruit-core: #ff9a1a;
    --fruit-edge: #f7b04a;
  }
  html, body {
    margin: 0;
    width: 1200px;
    height: 1200px;
    overflow: hidden;
    background: var(--page);
  }
  .canvas {
    width: 1200px;
    height: 1200px;
    display: flex;
    align-items: center;
    justify-content: center;
  }
  .billboard {
    width: 1160px;
    height: 349px;
    display: block;
  }
  .billboard__title {
    font-family: "Anton", "Oswald", sans-serif;
    fill: var(--white);
    letter-spacing: 1px;
  }
  .billboard__feature {
    font-family: "Barlow Condensed", "Arial Narrow", sans-serif;
    font-style: italic;
    font-weight: 700;
    fill: var(--white);
  }
  .billboard__phone {
    font-family: "Barlow Condensed", "Arial Narrow", sans-serif;
    font-style: italic;
    font-weight: 700;
    fill: var(--orange-deep);
  }
  .fill-white { fill: var(--white); }
  .fill-bright { fill: var(--orange-bright); }
  .fill-deep { fill: var(--orange-deep); }
  .fill-red { fill: var(--orange-red); }
  .fill-peach { fill: var(--peach); }
</style>
</head>
<body>
<main class="canvas">
  <svg class="billboard" viewBox="0 0 1395 420" xmlns="http://www.w3.org/2000/svg">
    <defs>
      <radialGradient id="fruitTone" cx="0.42" cy="0.45" r="0.6">
        <stop offset="0" stop-color="var(--fruit-core)"/>
        <stop offset="0.75" stop-color="var(--fruit-edge)"/>
        <stop offset="1" stop-color="var(--white)"/>
      </radialGradient>
    </defs>

    <rect class="fill-white" x="0" y="0" width="1395" height="420"/>

    <path class="billboard__photo" role="img"
          aria-label="Photo of a large whole orange with a cut orange wedge in front"
          fill="url(#fruitTone)"
          d="M0,0 L600,0 Q700,90 690,230 Q680,340 640,420 L0,420 Z"/>

    <path class="fill-bright" d="M735,0 L1395,0 L1395,420 L775,420 Q810,200 735,0 Z"/>
    <path class="fill-white" d="M740,0 L795,0 Q840,120 810,310 Q800,120 740,0 Z"/>
    <path class="fill-deep" d="M810,312 L1395,35 L1395,420 L775,420 Z"/>
    <path class="fill-peach" d="M680,0 L700,0 Q790,200 775,420 L700,420 Q745,200 680,0 Z"/>
    <path class="fill-red" d="M660,0 L682,0 Q748,200 682,420 L645,420 Q722,210 660,0 Z"/>
    <path class="fill-bright" d="M585,0 L628,0 Q690,90 678,195 Q652,80 585,0 Z"/>

    <path class="fill-white" d="M965,420 Q1070,310 1230,308 Q1330,310 1395,345 L1395,420 Z"/>

    <text class="billboard__title" x="1105" y="155" font-size="84"
          text-anchor="middle" textLength="520" lengthAdjust="spacingAndGlyphs">CEDAR BEND RV PARK</text>

    <rect class="fill-red" x="830" y="209" width="87" height="22" rx="11"/>
    <text class="billboard__feature" x="926" y="233" font-size="42"
          textLength="395" lengthAdjust="spacingAndGlyphs">Free Fiber Optic Internet</text>

    <rect class="fill-red" x="822" y="259" width="95" height="22" rx="11"/>
    <text class="billboard__feature" x="926" y="283" font-size="42"
          textLength="357" lengthAdjust="spacingAndGlyphs">Own Personal Hotspot</text>

    <text class="billboard__phone" x="1028" y="390" font-size="44"
          textLength="347" lengthAdjust="spacingAndGlyphs">Phone# 5550148273</text>
  </svg>
</main>
</body>
</html>
```